Referral Flyer Marketing Flyer 8.5" x 5.5" (Half Page) Front & Back

Designer Instructions – Updated Referral Program Flyer

(Based on the mock-up in “Brief Layout and Instructions.pdf”)

OVERALL STYLE + LAYOUT

Maintain the same general layout, structure, and flow as the mock-up flyer (front and back).

This is an update of an older flyer, not a full redesign — keep the same sections, proportions, and overall visual feel, but with cleaner, more modern design improvements.

The final flyer should look clean, bold, professional, and high-impact, geared toward realtors, property managers, and contractors who refer work.

FRONT SIDE INSTRUCTIONS
1. Header Section

Remove the Tidewell Renovation logo from the top banner.
(Shown on page 1 of the PDF)

2. Main Headline

Keep the same three-line structure:
EARN
UNLIMITED
CASH

Center it, maximize impact, and increase the font size of CASH so all three words match in importance.

Make the headline bold, clean, and the main focal point.

3. Cash Incentive Box

Keep the "$500 minimum OR 10% per referral" box, but upgrade the graphics to look sharper and more modern.

Ensure the wording matches exactly what’s in the mock-up.

4. Premier Partner Program Ribbon

Clean up and modernize the "PREMIER PARTNER PROGRAM" bar while keeping the same position and structure.

Ensure the checkmark badge remains crisp and professional.

5. Supporting Icons Section

Keep the four icons/benefit boxes (Guaranteed Payout, Free Evaluations, Affordable Solutions, Industry Leaders) in the same order.

Update the icons to cleaner, more modern styles — but maintain the same meanings.

Improve alignment and spacing for sharper visual consistency.

6. Remove Icons in Contact Area

At the bottom (“CALL TEXT OR BOOK ONLINE 858-472-6190 BrightKeelRebuilds.com”), remove the phone and internet icons, as noted on page 2 of the PDF.

7. Replace All Images

I (Dorian) will provide all updated stock images separately via email.

Replace the flood/water-damage imagery and roof leak with the new images I send.

Keep image placement and proportions the same as the mock-up.

BACK SIDE INSTRUCTIONS
1. Header Image + “REFER / EARN” Section

Maintain the same large split-image layout (“The more you refer, the more you earn”).

Replace all background imagery with the new assets I will send.

Keep the CASH FLOW image section but modernize the type and spacing.

2. “HOW IT WORKS” Section

Preserve the three-column layout:

Refer Flood, Water & Mold Damage

We Take Care of Everything (evaluations/insurance)

Get Paid to Share

Update images, tighten spacing, and use modern iconography.

3. Remove Phone/Internet Icons

Same as the front side — remove small communication icons and keep only the text/number/URL.

4. Bottom Contact Bar

Keep the blue bar, same wording, same layout — just modernize the style if needed for clarity.

5. Replace All Back-Side Images

Again, I will email you the image assets.

Keep the layout EXACT — just update with higher-quality photos and improved design.

TEXT CONTENT (Keep as-is unless spacing adjustments needed)

All text shown in the PDF should remain exactly the same unless spacing or visual balance requires minor adjustments.
Example from page 3:

“REFER FLOOD, MOLD & CONSTRUCTION JOBS”

“We Schedule a Free Estimate. If Approved, You Get Paid.”

“Everybody Benefits From Referrals”

Everything stays, just refreshed and visually improved.

DESIGN GOALS

Flyer should look high-end and trustworthy, not salesy.

Consistent color theme: blues, whites, yellows, same palette as original.

Use bold, modern fonts with strong readability.

Ensure all headlines pop and all benefit boxes are clean, well-aligned, and evenly spaced.

The final result should feel like a premium referral program flyer for a top-tier restoration/remodel company.

FILES I WILL PROVIDE

I will send the designer:

All replacement stock photos

Any updated logos (if needed)

Original high-resolution version of the mock-up (if available)

Any additional icons preferred

Colors
0054AA
0677BA
7BADD7
CADEEF
E8F1F8

Requirements
Must have
• Designer Instructions – Updated Referral Program Flyer (Based on the mock-up in “Brief Layout and Instructions.pdf”) OVERALL STYLE + LAYOUT Maintain the same general layout, structure, and flow as the mock-up flyer (front and back). This is an update of an older flyer, not a full redesign — keep the same sections, proportions, and overall visual feel, but with cleaner, more modern design improvements. The final flyer should look clean, bold, professional, and high-impact, geared toward realtors, property managers, and contractors who refer work. FRONT SIDE INSTRUCTIONS 1. Header Section Remove the Tidewell Renovation logo from the top banner. (Shown on page 1 of the PDF) 2. Main Headline Keep the same three-line structure: EARN UNLIMITED CASH Center it, maximize impact, and increase the font size of CASH so all three words match in importance. Make the headline bold, clean, and the main focal point. 3. Cash Incentive Box Keep the "$500 minimum OR 10% per referral" box, but upgrade the graphics to look sharper and more modern. Ensure the wording matches exactly what’s in the mock-up. 4. Premier Partner Program Ribbon Clean up and modernize the "PREMIER PARTNER PROGRAM" bar while keeping the same position and structure. Ensure the checkmark badge remains crisp and professional. 5. Supporting Icons Section Keep the four icons/benefit boxes (Guaranteed Payout, Free Evaluations, Affordable Solutions, Industry Leaders) in the same order. Update the icons to cleaner, more modern styles — but maintain the same meanings. Improve alignment and spacing for sharper visual consistency. 6. Remove Icons in Contact Area At the bottom (“CALL TEXT OR BOOK ONLINE 858-472-6190 BrightKeelRebuilds.com”), remove the phone and internet icons, as noted on page 2 of the PDF. 7. Replace All Images I (Dorian) will provide all updated stock images separately via email. Replace the flood/water-damage imagery and roof leak with the new images I send. Keep image placement and proportions the same as the mock-up. BACK SIDE INSTRUCTIONS 1. Header Image + “REFER / EARN” Section Maintain the same large split-image layout (“The more you refer, the more you earn”). Replace all background imagery with the new assets I will send. Keep the CASH FLOW image section but modernize the type and spacing. 2. “HOW IT WORKS” Section Preserve the three-column layout: Refer Flood, Water & Mold Damage We Take Care of Everything (evaluations/insurance) Get Paid to Share Update images, tighten spacing, and use modern iconography. 3. Remove Phone/Internet Icons Same as the front side — remove small communication icons and keep only the text/number/URL. 4. Bottom Contact Bar Keep the blue bar, same wording, same layout — just modernize the style if needed for clarity. 5. Replace All Back-Side Images Again, I will email you the image assets. Keep the layout EXACT — just update with higher-quality photos and improved design. TEXT CONTENT (Keep as-is unless spacing adjustments needed) All text shown in the PDF should remain exactly the same unless spacing or visual balance requires minor adjustments. Example from page 3: “REFER FLOOD, MOLD & CONSTRUCTION JOBS” “We Schedule a Free Estimate. If Approved, You Get Paid.” “Everybody Benefits From Referrals” Everything stays, just refreshed and visually improved. DESIGN GOALS Flyer should look high-end and trustworthy, not salesy. Consistent color theme: blues, whites, yellows, same palette as original. Use bold, modern fonts with strong readability. Ensure all headlines pop and all benefit boxes are clean, well-aligned, and evenly spaced. The final result should feel like a premium referral program flyer for a top-tier restoration/remodel company. FILES I WILL PROVIDE I will send the designer: All replacement stock photos Any updated logos (if needed) Original high-resolution version of the mock-up (if available) Any additional icons preferred

```html
<!DOCTYPE html>
<html lang="en">
<head>
<meta charset="utf-8">
<title>Referral Program Flyer – Front &amp; Back</title>
<link href="https://fonts.googleapis.com/css2?family=Poppins:wght@400;500;600;700;800&family=Anton&display=swap" rel="stylesheet">
<style>
  :root{
    --navy:#0a2a66;
    --navy-deep:#12213a;
    --blue:#34609a;
    --yellow:#fcc21b;
    --red:#d93a35;
    --red-deep:#b21a1a;
    --slate:#7b8b9c;
    --white:#ffffff;
    --stage:#b3b3b3;
    --ink:#1d2b4a;
  }
  *{box-sizing:border-box;margin:0;padding:0}
  html,body{width:898px;height:1200px;overflow:hidden}
  body{background:var(--stage);font-family:"Poppins",sans-serif;position:relative}
  .card{position:absolute;left:61px;width:775px;height:502px;background:var(--white);overflow:hidden;box-shadow:0 4px 14px rgba(0,0,0,.25)}
  .card--front{top:69px}
  .card--back{top:629px}
  .abs{position:absolute}

  /* header */
  .header-art{position:absolute;left:0;top:0;width:775px;height:222px}
  .headline{position:absolute;left:111px;top:20px;width:200px;text-align:center;font-weight:800;line-height:1;}
  .headline .big{display:block;color:var(--yellow);font-size:44px;letter-spacing:1px}
  .headline .mid{display:block;color:var(--white);font-size:33px;margin:4px 0 6px}
  .banner{position:absolute;height:40px;background:var(--yellow);color:var(--navy);font-weight:700;display:flex;align-items:center;clip-path:polygon(0 0,100% 0,95% 100%,0 100%)}
  .banner--flood{left:46px;top:170px;width:405px;padding-left:20px;font-size:23px;letter-spacing:.8px}
  .banner--how{left:46px;top:200px;width:241px;padding-left:20px;font-size:23px;letter-spacing:.5px}

  /* incentive pills */
  .pill{position:absolute;top:236px;height:60px;border-radius:30px;color:var(--white);font-weight:700;display:flex;align-items:center}
  .pill--min{left:46px;width:146px;background:var(--red);flex-direction:column;justify-content:center;align-items:flex-start;padding-left:24px;line-height:1}
  .pill--min .amt{font-size:21px}
  .pill--min .lbl{font-size:13px;margin-top:3px}
  .pill--pct{left:170px;width:211px;background:#c42a2a;padding-left:42px;gap:10px}
  .pill--pct .amt{font-size:25px}
  .pill--pct .lbl{font-size:12px;line-height:1.45}
  .pill--partner{left:395px;width:170px;background:var(--red-deep);font-size:20px;letter-spacing:1px;padding-left:24px}
  .pill--program{left:555px;width:174px;background:var(--slate);font-size:20px;letter-spacing:1px;padding-left:40px}
  .or-badge{position:absolute;left:152px;top:236px;width:60px;height:60px;border-radius:50%;background:var(--white);border:3px solid var(--yellow);color:var(--navy);font-weight:700;font-size:19px;display:flex;align-items:center;justify-content:center}
  .check-badge{position:absolute;left:532px;top:236px;width:60px;height:60px;border-radius:50%;background:var(--white);border:3px solid var(--yellow);display:flex;align-items:center;justify-content:center}
  .premier-tab{position:absolute;left:514px;top:211px;width:97px;height:21px;border-radius:11px 11px 0 0;background:var(--white);color:var(--navy);font-size:13px;font-weight:500;text-align:center;line-height:23px;box-shadow:0 -1px 2px rgba(0,0,0,.08)}

  .subhead{position:absolute;left:0;width:775px;top:308px;text-align:center;color:var(--navy);font-weight:700;font-size:18.5px;letter-spacing:.3px}

  /* benefit boxes */
  .benefit{position:absolute;top:340px;width:136px;height:85px;border:1.5px solid #8a96aa;border-radius:10px}
  .benefit::after{content:"";position:absolute;right:8px;bottom:-3px;width:5px;height:5px;border-radius:50%;background:var(--navy)}
  .benefit__title{position:absolute;left:-1px;top:-1px;width:136px;height:36px;border:3px solid var(--navy);border-radius:10px;background:var(--white);display:flex;align-items:center;justify-content:center;text-align:center;font-size:8.5px;font-weight:600;line-height:1.2;letter-spacing:.5px}
  .benefit:nth-child(odd) .benefit__title{color:var(--navy)}
  .benefit__title--muted{color:var(--blue)}
  .benefit__text{position:absolute;left:11px;top:43px;width:92px;font-size:7.6px;line-height:1.4;font-weight:500;color:var(--ink)}
  .benefit__icon{position:absolute;right:-6px;top:42px}
  .b1{left:83px}.b2{left:238px}.b3{left:394px}.b4{left:549px}

  .tagline{position:absolute;left:0;width:775px;top:434px;text-align:center;font-weight:700;font-size:14.5px;letter-spacing:.6px;color:var(--navy)}
  .tagline em{font-style:normal;color:var(--red-deep)}

  /* contact bar */
  .contact{position:absolute;left:0;top:461px;width:775px;height:41px}
  .contact__bar{position:absolute;left:0;top:0;width:317px;height:41px;background:var(--navy);clip-path:polygon(0 0,94% 0,100% 100%,0 100%);color:var(--yellow);font-size:15.5px;font-weight:500;display:flex;align-items:center;padding-left:45px}
  .contact__info{position:absolute;left:353px;top:0;height:41px;display:flex;align-items:center;gap:12px;color:var(--navy);font-size:17.5px;font-weight:500}

  /* back headline */
  .refer-head{position:absolute;left:106px;top:18px;width:150px;text-align:center;font-family:"Anton",sans-serif;line-height:.98;text-transform:uppercase}
  .refer-head .small{display:block;color:var(--white);font-size:24px}
  .refer-head .huge{display:block;font-size:60px;background:linear-gradient(180deg,#fff04a,#f2b21a 70%,#e8991c);-webkit-background-clip:text;background-clip:text;color:transparent}

  /* steps */
  .step{position:absolute;top:258px;width:208px;height:189px;border:1.5px solid var(--navy);border-radius:14px;text-align:center}
  .step__photo{position:absolute;left:6px;top:6px;width:194px;height:108px;border-radius:9px}
  .step__title{position:absolute;left:0;width:100%;top:120px;color:var(--navy);font-weight:700;font-size:11.2px;line-height:1.32;letter-spacing:.6px}
  .step__text{position:absolute;left:0;width:100%;top:152px;color:#222;font-size:10px;line-height:1.4;letter-spacing:.3px}
  .s1{left:62px}.s2{left:284px}.s3{left:505px}
  .step:nth-child(3) .step__title{color:var(--blue)}
</style>
</head>
<body>

<!-- FRONT -->
<section class="card card--front" aria-label="Front side">
  <svg class="header-art" viewBox="0 0 775 222" aria-hidden="false">
    <polygon points="0,0 439,0 388,111 445,222 0,222" fill="var(--navy)"/>
    <polygon points="445,0 775,0 775,222 451,222 394,111" fill="#ffffff"/>
    <g role="img" aria-label="Photo of a bright remodeled kitchen with navy cabinets and white counters">
      <defs>
        <linearGradient id="kitchen" x1="0" y1="0" x2="0" y2="1">
          <stop offset="0" stop-color="#e8e5df"/>
          <stop offset=".55" stop-color="#d9d5ce"/>
          <stop offset=".7" stop-color="#4b5a78"/>
          <stop offset="1" stop-color="#5a3a2a"/>
        </linearGradient>
      </defs>
      <polygon points="450,0 775,0 775,222 456,222 400,111" fill="url(#kitchen)"/>
    </g>
  </svg>
  <h1 class="headline"><span class="big">EARN</span><span class="mid">UNLIMITED</span><span class="big">CASH</span></h1>
  <div class="banner banner--flood">GET PAID TO REFER A FLOOD</div>

  <div class="premier-tab">PREMIER</div>
  <div class="pill pill--min"><span class="amt">$500</span><span class="lbl">MINIMUM</span></div>
  <div class="pill pill--pct"><span class="amt">10%</span><span class="lbl">PER<br>REFERRAL!</span></div>
  <div class="or-badge">OR</div>
  <div class="pill pill--partner">PARTNER</div>
  <div class="pill pill--program">PROGRAM</div>
  <div class="check-badge">
    <svg width="32" height="32" viewBox="0 0 32 32"><circle cx="15" cy="17" r="11" fill="none" stroke="var(--navy)" stroke-width="3"/><path d="M9 16l5 6L28 5" fill="none" stroke="var(--navy)" stroke-width="3.5" stroke-linecap="round" stroke-linejoin="round"/></svg>
  </div>

  <h2 class="subhead">PARTNER WITH US &amp; EVERYBODY WINS!</h2>

  <div class="benefits">
    <div class="benefit b1">
      <div class="benefit__title">GUARANTEED<br>PAYOUT*</div>
      <p class="benefit__text">Minimum $500 or 10% of Total Invoice Paid Fast</p>
      <svg class="benefit__icon" width="34" height="36" viewBox="0 0 34 36"><path d="M17 2l3 7 7 .5-5.5 4.5 2 7-6.5-4-6.5 4 2-7L7 9.5l7-.5z" fill="var(--yellow)"/><rect x="10" y="24" width="14" height="11" rx="2" fill="var(--yellow)"/></svg>
    </div>
    <div class="benefit b2">
      <div class="benefit__title">FREE<br>ESTIMATES</div>
      <p class="benefit__text">Fast &amp; Free Inspections &amp; Written Estimates</p>
      <svg class="benefit__icon" width="32" height="36" viewBox="0 0 32 36"><rect x="3" y="2" width="22" height="30" rx="3" fill="var(--yellow)"/><rect x="6" y="5" width="16" height="6" fill="#fff"/><g fill="#fff"><rect x="6" y="14" width="4" height="4"/><rect x="12" y="14" width="4" height="4"/><rect x="18" y="14" width="4" height="4"/><rect x="6" y="20" width="4" height="4"/><rect x="12" y="20" width="4" height="4"/><rect x="18" y="20" width="4" height="4"/></g><circle cx="26" cy="27" r="6" fill="var(--navy)"/></svg>
    </div>
    <div class="benefit b3">
      <div class="benefit__title benefit__title--muted">AFFORDABLE<br>SOLUTIONS</div>
      <p class="benefit__text">Lowest Out of Pocket Costs for Your Customers</p>
      <svg class="benefit__icon" width="34" height="36" viewBox="0 0 34 36"><circle cx="18" cy="15" r="11" fill="var(--yellow)"/><text x="18" y="20" text-anchor="middle" font-family="Poppins,sans-serif" font-size="14" font-weight="700" fill="#fff">$</text><rect x="3" y="28" width="20" height="6" rx="3" fill="var(--yellow)"/></svg>
    </div>
    <div class="benefit b4">
      <div class="benefit__title benefit__title--muted">INDUSTRY<br>LEADERS</div>
      <p class="benefit__text">Licensed &amp; Certified Experts Provide 100% Guarantee</p>
      <svg class="benefit__icon" width="34" height="36" viewBox="0 0 34 36"><circle cx="17" cy="20" r="11" fill="none" stroke="var(--yellow)" stroke-width="5" stroke-dasharray="4 3"/><circle cx="17" cy="20" r="6" fill="var(--yellow)"/><circle cx="17" cy="5" r="3" fill="var(--yellow)"/><circle cx="8" cy="8" r="2.5" fill="var(--yellow)"/><circle cx="26" cy="8" r="2.5" fill="var(--yellow)"/></svg>
    </div>
  </div>

  <p class="tagline">SEND <em>REFERRALS</em>. GET <em>PAID</em>. GROW <em>YOUR BUSINESS.</em></p>

  <footer class="contact">
    <div class="contact__bar">CALL, TEXT OR BOOK ONLINE</div>
    <div class="contact__info"><span>858-472-6190</span><span>www.BrightKeelRebuilds.com</span></div>
  </footer>
</section>

<!-- BACK -->
<section class="card card--back" aria-label="Back side">
  <svg class="header-art" viewBox="0 0 775 222">
    <rect x="0" y="0" width="430" height="222" fill="var(--blue)"/>
    <polygon points="230,0 347,0 429,222 150,222 180,160" fill="var(--navy-deep)"/>
    <polygon points="220,15 560,15 429,222 330,222" fill="var(--navy-deep)"/>
    <polygon points="340,0 775,0 775,222 429,222" fill="#ffffff"/>
    <g role="img" aria-label="Photo of hundred-dollar bills with letter tiles spelling cash flow">
      <defs>
        <linearGradient id="bills" x1="0" y1="0" x2="1" y2="1">
          <stop offset="0" stop-color="#cfd3cc"/>
          <stop offset=".5" stop-color="#b7bdb3"/>
          <stop offset="1" stop-color="#9ea69c"/>
        </linearGradient>
      </defs>
      <polygon points="346,0 775,0 775,222 433,222" fill="url(#bills)"/>
    </g>
  </svg>
  <h1 class="refer-head"><span class="small">The more you</span><span class="huge">Refer</span><span class="small">The more you</span><span class="huge">Earn</span></h1>
  <div class="banner banner--how">HOW IT WORKS</div>

  <div class="steps">
    <div class="step s1">
      <div class="step__photo" role="img" aria-label="Photo of a leaking pipe under a sink" style="background:linear-gradient(135deg,#5b5a58,#d8d8d6 60%,#f2f2f0)"></div>
      <h3 class="step__title">REFER FLOOD, MOLD &amp;<br>CONSTRUCTION JOBS</h3>
      <p class="step__text">It’s Simple to Refer 24/7:<br>Call, Text or Book Online.</p>
    </div>
    <div class="step s2">
      <div class="step__photo" role="img" aria-label="Photo of an inspector holding a work estimate clipboard in front of a house" style="background:linear-gradient(135deg,#4f6b3a,#8a7a6a 55%,#c9d2dc)"></div>
      <h3 class="step__title">WE TAKE CARE OF<br>EVERYTHING</h3>
      <p class="step__text">We Schedule a Free Estimate.<br>If Approved, You Get Paid.</p>
    </div>
    <div class="step s3">
      <div class="step__photo" role="img" aria-label="Photo of a yellow road sign reading get paid to share against a blue sky" style="background:linear-gradient(135deg,#5b8fd0,#cfe0f2 55%,#8fb6e2)"></div>
      <h3 class="step__title">EVERYBODY BENEFITS<br>FROM REFERRALS</h3>
      <p class="step__text">We Provide Expert Quality<br>Work for Affordable Price.</p>
    </div>
  </div>

  <footer class="contact">
    <div class="contact__bar">CALL, TEXT OR BOOK ONLINE</div>
    <div class="contact__info"><span>858-472-6190</span><span>www.BrightKeelRebuilds.com</span></div>
  </footer>
</section>

</body>
</html>
```